Ushuaia site

create new design for the site Uhsuaia brelocanto.inf.br
Our benchmark is www.trekvalemo.com
We want a big banner in the center, with huge images as well.
Background must be white.
Must have a sitemap on footer.
Menu "fique por dentro" must be transformed into a horizontal upper menu.
We need: newsletter sign-up field, Zirpex +, WorkTally.
We also need space for ads: square ads in the lateral side, and banners on the upper part.
Please use solely the attached photos to create the layout.

*the current layout is very confusing, something we must fix in the new one.
The vertical menu on the right MUST BE THE HORIZONTAL MENU ON THE TOP ON THE NEW SITE.
The current vertical menu on the left, can either stay vertical on the left, or go to the right, or be transformed into another element, but CAN NEVER BECOME THE PRINCIPAL MENU OF THE SITE ON THE TOP HORIZONTALLY.

*we currently don't have a specific logo, so feel free to create something, but don't worry to elaborate, because we are just a content site as of now.
Since it's a location site, we wouldn't like elements such as planes, passports, etc, associated, because they remind people of travel agencies, which we are not, we are just a destination specialist.
But feel free to use a special font, or some image that associate with Ushuaia, such as mountains, wood signs of the "fin del mundo", etc.

Target Market(s)

travellers who go to Ushuaia and the Patagonia region, and would like to design the tour themselves.

Industry/Entity Type

Travel

Coding

Coded - Design and coding required

Font styles to use
Sans Serif

Colors
ffffff
3176b5
fde08a
0555a3

Requirements
Must have
• * huge banner with images on top for the homepage;
* horizontal menu;
* sign-up for newsletter;
* logos for Zirpex +, and WorkTally;
* footer;
* space for ads.
* We need design for only 3 model pages: homepage, content page, form page (basically the same as content, but with the form).
* html will have to be done for all currently existing pages.
Should not have
• * pebblecast logo;
* intranet area.

```html
<!DOCTYPE html>
<html lang="en">
<head>
<meta charset="utf-8">
<title>Brelocanto – Ushuaia Travel Guide</title>
<link href="https://fonts.googleapis.com/css2?family=Open+Sans:wght@300;400;600;700&display=swap" rel="stylesheet">
<style>
:root{
  --white:#ffffff;
  --brand:#0555a3;
  --blue:#3176b5;
  --blue-deep:#0555a3;
  --yellow:#fde08a;
  --yellow-strong:#f3c23c;
  --ink:#2b2f33;
  --text:#555b61;
  --muted:#9aa0a6;
  --line:#e3e5e8;
  --panel:#f4f5f6;
  --score:#e8683a;
  --footer:#2d3035;
  --footer-deep:#25282c;
  --footer-line:#3b3f45;
  --footer-text:#a8adb3;
}
*{box-sizing:border-box;margin:0;padding:0}
html,body{width:1200px;height:3468px;overflow:hidden;background:var(--white)}
body{font-family:"Open Sans",Arial,sans-serif;color:var(--text);position:relative}
.abs{position:absolute}

/* header */
.site-name{left:128px;top:72px;display:flex;align-items:center;gap:12px;font-size:34px;font-weight:600;color:var(--brand);line-height:40px}
.site-name i{display:block;width:14px;height:14px;border-radius:50%;background:var(--blue)}
.ad-leaderboard{left:711px;top:49px;width:364px;height:76px;border:1px solid var(--line);display:flex;align-items:center;justify-content:center;color:#c4c8cc;font-size:22px;font-weight:300;letter-spacing:1px}
.ad-leaderboard b{font-weight:400;margin-left:14px}
.main-nav{left:128px;top:148px;width:947px;height:32px;display:flex;border-bottom:1px solid var(--line)}
.main-nav a{display:block;font-size:12px;color:var(--ink);text-decoration:none;padding:6px 0 0 12px;width:90px;position:relative}
.main-nav a::after{content:"";position:absolute;left:0;right:10px;bottom:-1px;height:3px;background:var(--c,var(--blue))}
.nav-search{left:1070px;top:156px}

/* hero */
.hero{left:0;top:215px;width:1200px;height:427px;background:linear-gradient(180deg,#c9c7c0 0%,#9b948a 45%,#6e665d 75%,#544d45 100%)}
.hero-title{left:120px;top:340px;font-size:31px;font-weight:400;line-height:42px;color:var(--white);text-transform:uppercase;letter-spacing:.5px}
.hero-title span{background:rgba(30,28,26,.45);padding:0 8px}

/* section heads */
.section-head{left:128px;width:635px;border-bottom:1px solid var(--line);height:52px}
.section-head h2{font-size:31px;font-weight:300;color:var(--ink)}
.section-head .more{position:absolute;right:16px;top:8px;font-size:9px;color:var(--muted);border:1px solid var(--line);padding:5px 12px}

/* cards */
.card{width:305px}
.thumb{width:305px;height:125px}
.card h3{font-size:15px;font-weight:400;color:var(--ink);line-height:20px;margin-top:22px}
.meta{display:flex;align-items:center;gap:6px;font-size:9px;color:var(--muted);margin-top:7px}
.tag{background:var(--yellow);color:var(--ink);font-size:8px;font-weight:700;padding:1px 6px;text-transform:uppercase}
.tag.blue{background:var(--blue);color:var(--white)}
.stars{color:var(--yellow-strong);font-size:10px;letter-spacing:1px}
.excerpt{font-size:10px;line-height:15px;color:var(--muted);margin-top:8px;width:290px}
.score{position:absolute;width:40px;height:40px;border:3px solid var(--score);border-radius:50%;color:var(--score);font-size:12px;font-weight:700;display:flex;align-items:center;justify-content:center;background:var(--white)}

.mini{display:flex;gap:14px;width:305px}
.mini .sq{width:62px;height:62px;flex:none}
.mini h4{font-size:13px;font-weight:400;color:var(--ink);line-height:18px;margin-top:4px}

/* sidebar */
.sidebar{left:798px;top:690px;width:277px;height:2230px;background:var(--panel)}
.side-search{left:812px;top:712px;width:249px;height:30px;background:var(--white);border:1px solid var(--line);font-size:10px;color:var(--muted);padding:8px 10px}
.side-head{left:822px;font-size:14px;color:var(--ink);font-weight:400}
.side-post{left:822px;width:230px}
.side-post p{font-size:10px;color:var(--ink);line-height:14px}
.side-post .meta{margin-top:3px}
.calendar{left:822px;top:1076px;width:236px;border-collapse:collapse;font-size:9px;color:var(--text)}
.calendar caption{font-size:11px;color:var(--ink);padding-bottom:12px}
.calendar th{background:#dfe2e5;height:34px;font-weight:600;color:var(--ink);border:2px solid var(--panel)}
.calendar td{background:var(--white);height:42px;text-align:right;vertical-align:top;padding:4px;border:2px solid var(--panel)}
.calendar td.empty{background:transparent}
.calendar td.on{background:var(--yellow)}
.cal-nav{left:822px;top:1074px;display:flex;gap:4px}
.cal-nav i{display:block;width:18px;height:18px;border:1px solid var(--line);background:var(--white)}
.side-list{left:822px;width:230px;list-style:none;font-size:10px;color:var(--ink)}
.side-list li{padding:5px 0 5px 12px;position:relative;line-height:14px}
.side-list li::before{content:"";position:absolute;left:0;top:10px;width:4px;height:4px;background:var(--blue);border-radius:50%}
.side-thumbs{left:822px;width:240px}
.side-thumbs .row{display:flex;gap:10px;margin-bottom:10px}
.side-thumbs .sq{width:34px;height:34px;flex:none}
.side-thumbs p{font-size:9px;color:var(--ink);line-height:13px}

.ad-square{left:812px;top:2420px;width:249px;height:249px;background:var(--white);border:1px solid var(--line);display:flex;align-items:center;justify-content:center;flex-direction:column;color:#c4c8cc;font-size:18px;font-weight:300}
.ad-square b{font-weight:400;font-size:14px;margin-top:4px}
.newsletter{left:822px;top:2700px;width:230px}
.newsletter p{font-size:10px;color:var(--muted);line-height:14px;margin:10px 0}
.newsletter .field{height:30px;border:1px solid var(--line);background:var(--white);font-size:10px;color:var(--muted);padding:8px 10px}
.newsletter .btn{margin-top:6px;height:30px;background:var(--blue);color:var(--white);font-size:11px;font-weight:600;text-align:center;line-height:30px;text-transform:uppercase}
.follow{left:822px;top:2860px;display:flex;gap:26px;font-size:11px;color:var(--ink)}
.follow span{display:flex;align-items:center;gap:8px}
.follow i{display:block;width:12px;height:12px;background:var(--blue)}
.follow i.round{border-radius:50%;background:var(--score)}

/* footer */
.footer{left:0;top:2972px;width:1200px;height:496px;background:var(--footer)}
.f-head{top:3022px;font-size:11px;color:var(--white);border-bottom:1px solid var(--footer-line);padding-bottom:10px;width:220px}
.f-post{display:flex;gap:10px;width:220px;margin-bottom:12px}
.f-post .sq{width:34px;height:34px;flex:none}
.f-post p{font-size:9px;color:var(--footer-text);line-height:13px}
.f-post .stars{font-size:8px}
.photo-grid{left:381px;top:3062px;display:grid;grid-template-columns:repeat(3,56px);gap:6px}
.photo-grid div{height:56px}
.tweet{display:flex;gap:10px;width:220px;margin-bottom:18px}
.tweet svg{flex:none;margin-top:2px}
.tweet p{font-size:9px;color:var(--footer-text);line-height:13px}
.tweet p span{color:#6f9fd0}
.tweet small{display:block;font-size:8px;color:#6e7379;margin-top:3px}
.weather-now{left:884px;top:3070px;width:200px;display:flex;align-items:center;gap:20px}
.weather-now b{font-size:56px;font-weight:300;color:var(--white)}
.weather-now b sup{font-size:22px}
.weather-now p{font-size:9px;color:var(--footer-text);line-height:13px}
.weather-days{left:884px;top:3158px;display:flex;gap:4px}
.weather-days div{width:62px;height:56px;background:#41464d;color:var(--white);text-align:center;font-size:22px;font-weight:300;padding-top:6px}
.weather-days small{display:block;font-size:8px;color:var(--footer-text)}

.sitemap{left:128px;top:3275px;width:947px;border-top:1px solid var(--footer-line);padding-top:22px;display:flex;gap:60px}
.sitemap h5{font-size:11px;color:var(--white);font-weight:600;margin-bottom:10px}
.sitemap ul{list-style:none;font-size:10px;color:var(--footer-text);line-height:18px}
.bottom-bar{left:0;top:3418px;width:1200px;height:50px;background:var(--footer-deep);font-size:10px;color:#7d8288;padding:18px 128px;display:flex;justify-content:space-between}
</style>
</head>
<body>

<header>
  <div class="abs site-name"><i></i>brelocanto</div>
  <div class="abs ad-leaderboard">leaderboard <b>728 x 90</b></div>
  <nav class="abs main-nav">
    <a href="#" style="--c:var(--yellow-strong)">Home</a>
    <a href="#" style="--c:var(--blue)">Headers</a>
    <a href="#" style="--c:#7fb24c">Sliders</a>
    <a href="#" style="--c:var(--score)">Features</a>
    <a href="#" style="--c:var(--blue-deep)">Blog</a>
    <a href="#" style="--c:#9a64b8">Reviews</a>
    <a href="#" style="--c:#3bb3b0">Gallery</a>
  </nav>
  <svg class="abs nav-search" width="12" height="12" viewBox="0 0 12 12"><circle cx="5" cy="5" r="3.5" fill="none" stroke="#777" stroke-width="1.4"/><line x1="7.6" y1="7.6" x2="11" y2="11" stroke="#777" stroke-width="1.4"/></svg>
</header>

<div class="abs hero" role="img" aria-label="Photo of sea lions resting on rocks on the Beagle Channel near Ushuaia"></div>
<h1 class="abs hero-title"><span>Travel guide to Patagonia , all you need</span><br><span>to know for your trip to Ushuaia</span></h1>

<main>
  <div class="abs section-head" style="top:690px"><h2>Recent Posts</h2><span class="more">All News</span></div>

  <article class="abs card" style="left:128px;top:770px">
    <div class="thumb" role="img" aria-label="Photo of a red and white lighthouse on a rocky islet" style="background:linear-gradient(180deg,#7fb0dc,#2e5f93)"></div>
    <h3>You CAN Touch This: Rapper Dex Malone Tells Museums How It</h3>
    <div class="meta"><span class="tag">News</span><span>October 4, 2014</span><span class="stars">★★★★★</span></div>
    <p class="excerpt">Aenean magna tellus, rhoncus quis facilisis at, rutrum a augue. Donec at [...]</p>
  </article>
  <article class="abs card" style="left:451px;top:770px">
    <div class="thumb" role="img" aria-label="Photo of clock gears close up" style="background:linear-gradient(135deg,#d9d9d9,#8c8c8c)"></div>
    <h3>"Lick Boy Fat Art" Lenn Arvo's Language Art Decoded</h3>
    <div class="meta"><span class="tag">News</span><span>October 4, 2014</span><span class="stars">★★★★★</span></div>
    <p class="excerpt">Aenean magna tellus, rhoncus quis facilisis at, rutrum a augue. Donec at [...]</p>
  </article>
  <article class="abs card" style="left:128px;top:1096px">
    <div class="thumb" role="img" aria-label="Photo of a sunbather on a beach" style="background:linear-gradient(135deg,#aedbe6,#e9d8c4)"></div>
    <h3>How Mira Tovesk and Odd Halvan Got 35,000 People to Draw on the Moon</h3>
    <div class="meta"><span class="tag">News</span><span>October 4, 2014</span><span class="stars">★★★★★</span></div>
    <p class="excerpt">Aenean magna tellus, rhoncus quis facilisis at, rutrum a augue. Donec at [...]</p>
  </article>
  <article class="abs card" style="left:451px;top:1096px">
    <div class="thumb" role="img" aria-label="Photo of a horse running on a plain" style="background:linear-gradient(180deg,#f1ece6,#c79b6b)"></div>
    <h3>Most-Read Galleryline Posts in 2013–The Top 5</h3>
    <div class="meta"><span class="tag">News</span><span>October 4, 2014</span><span class="stars">★★★★★</span></div>
    <p class="excerpt">Aenean magna tellus, rhoncus quis facilisis at, rutrum a augue. Donec at [...]</p>
  </article>

  <div class="abs section-head" style="top:1530px"><h2>Various Styles</h2><span class="more">All posts</span></div>

  <article class="abs card" style="left:128px;top:1613px">
    <div class="thumb" style="height:138px;background:linear-gradient(180deg,#cf9a6a,#8a5a3a)" role="img" aria-label="Photo of red desert rock formations"></div>
    <h3 style="margin-top:12px">Claytimel Ceramics Finds its Place in the Art World Mainstream</h3>
    <div class="meta"><span class="tag">News</span><span>October 4, 2014</span><span class="stars">★★★★★</span></div>
  </article>
  <article class="abs card" style="left:451px;top:1613px">
    <div class="thumb" style="height:138px;background:linear-gradient(180deg,#bfe4ee,#3f9fb8)" role="img" aria-label="Photo of a tropical beach with palm trees"></div>
    <h3 style="margin-top:12px">It's All About Small Details</h3>
    <div class="meta"><span class="tag blue">Tips</span><span>October 4, 2014</span><span class="stars">★★★★★</span></div>
    <p class="excerpt">Aenean eleifend, mauris nec egestas ipsum quis facilisis sed, rutrum a augue.</p>
  </article>

  <div class="abs mini" style="left:128px;top:1905px"><div class="sq" role="img" aria-label="Photo of a green leaf" style="background:#4c7a3a"></div><div><h4>Friendly Design</h4><div class="meta"><span class="tag">News</span><span class="stars">★★★★★</span></div></div></div>
  <div class="abs mini" style="left:451px;top:1905px"><div class="sq" role="img" aria-label="Photo of a music player" style="background:#3a3e44"></div><div><h4>Music Should Be Easy</h4><div class="meta"><span class="tag">News</span><span class="stars">★★★★★</span></div></div></div>
  <div class="abs mini" style="left:128px;top:2000px"><div class="sq" role="img" aria-label="Photo of a silhouette at sunset" style="background:#d98a3a"></div><div><h4>Upcoming Events</h4><div class="meta"><span class="tag">News</span><span class="stars">★★★★★</span></div></div></div>
  <div class="abs mini" style="left:451px;top:2000px"><div class="sq" role="img" aria-label="Photo of fresh vegetables" style="background:#7aa84a"></div><div><h4>Healthy Food is a Guarantee of Good Mood</h4><div class="meta"><span class="tag">News</span><span class="stars">★★★★★</span></div></div></div>

  <div class="abs section-head" style="top:2240px"><h2>Most Popular Reviews</h2><span class="more">All Reviews</span></div>

  <article class="abs card" style="left:128px;top:2327px">
    <div class="thumb" style="height:128px;background:linear-gradient(180deg,#a9d6e8,#e2cbb4)" role="img" aria-label="Photo of a runner by the sea"></div>
    <h3 style="margin-top:34px">Reshooting 'Night Harbor' as Art</h3>
    <div class="meta"><span class="tag">Review</span><span>October 4, 2014</span><span class="stars">★★★★★</span></div>
    <p class="excerpt">Aenean magna tellus, rhoncus quis facilisis at, rutrum a augue. Donec at ipsum eleifend [...]</p>
  </article>
  <div class="score" style="left:388px;top:2470px">3.5</div>
  <article class="abs card" style="left:451px;top:2327px">
    <div class="thumb" style="height:128px;background:linear-gradient(135deg,#6b7a8a,#2f3a46)" role="img" aria-label="Photo of business people in a meeting"></div>
    <h3 style="margin-top:34px">Fakers, Fakes, &amp; Fake Fakers</h3>
    <div class="meta"><span class="tag">Review</span><span>October 4, 2014</span><span class="stars">★★★★★</span></div>
    <p class="excerpt">Aenean magna tellus, rhoncus quis facilisis at, rutrum a augue. Donec at ipsum eleifend [...]</p>
  </article>
  <div class="score" style="left:711px;top:2470px">3.9</div>

  <article class="abs card" style="left:128px;top:2677px">
    <div class="thumb" style="height:133px;background:linear-gradient(135deg,#e3d9cf,#8a6f5c)" role="img" aria-label="Photo of a group of friends at a table"></div>
    <h3 style="margin-top:28px">The Latest Varello Debate</h3>
    <div class="meta"><span class="tag">Review</span><span>October 4, 2014</span><span class="stars">★★★★★</span></div>
  </article>
  <div class="score" style="left:388px;top:2825px">3.0</div>
  <article class="abs card" style="left:451px;top:2677px">
    <div class="thumb" style="height:133px;background:linear-gradient(135deg,#eef3f8,#8fb3d6)" role="img" aria-label="Photo of charts printed on paper"></div>
    <h3 style="margin-top:28px">Events in Your Area</h3>
    <div class="meta"><span class="tag blue">Review</span><span>October 4, 2014</span><span class="stars">★★★★★</span></div>
    <p class="excerpt">Fusce rutrum convallis ligula, id condimentum nibh sed, eleifend ut quam at tellus [...]</p>
  </article>
  <div class="score" style="left:711px;top:2825px">3.6</div>
</main>

<aside>
  <div class="abs sidebar"></div>
  <div class="abs side-search">Search</div>

  <h3 class="abs side-head" style="top:790px">Most Commented</h3>
  <div class="abs side-post" style="top:832px"><p>Standard Post Format</p><div class="meta"><span class="stars">★★★★★</span><span>October 4, 2014</span></div></div>
  <div class="abs side-post" style="top:892px"><p>Better Over Than In</p><div class="meta"><span class="stars">★★★★★</span><span>October 4, 2014</span></div></div>
  <div class="abs side-post" style="top:952px"><p>New York Traffic Reports, Live Traffic &amp; Road Conditions</p><div class="meta"><span class="stars">★★★★★</span><span>October 4, 2014</span></div></div>
  <div class="abs side-post" style="top:1026px"><p>Video Post Example</p></div>

  <div class="abs cal-nav"><i></i><i></i></div>
  <table class="abs calendar">
    <caption>October 2014</caption>
    <tr><th>M</th><th>T</th><th>W</th><th>T</th><th>F</th><th>S</th><th>S</th></tr>
    <tr><td class="empty"></td><td class="empty"></td><td>1</td><td>2</td><td>3</td><td>4</td><td>5</td></tr>
    <tr><td>6</td><td>7</td><td>8</td><td>9</td><td>10</td><td>11</td><td>12</td></tr>
    <tr><td>13</td><td>14</td><td class="on">15</td><td>16</td><td>17</td><td>18</td><td>19</td></tr>
    <tr><td>20</td><td>21</td><td>22</td><td>23</td><td>24</td><td>25</td><td>26</td></tr>
    <tr><td>27</td><td>28</td><td>29</td><td>30</td><td>31</td><td class="empty"></td><td class="empty"></td></tr>
  </table>

  <h3 class="abs side-head" style="top:1404px">Recent Posts</h3>
  <ul class="abs side-list" style="top:1436px">
    <li>Review post (content overflow)</li>
    <li>Review post with sidebar</li>
    <li>New York Traffic Reports, Live Traffic &amp; Road Conditions</li>
    <li>Post slider is a convenient way to display posts from the blog</li>
    <li>Post slider module possibility flexible settings for posts</li>
  </ul>

  <div class="abs side-thumbs" style="top:1728px">
    <div class="row"><div class="sq" role="img" aria-label="Photo thumbnail" style="background:#8a6f5c"></div><p>Review post (content overflow)<br><span class="stars">★★★★★</span></p></div>
    <div class="row"><div class="sq" role="img" aria-label="Photo thumbnail" style="background:#5d7e9c"></div><p>Review post with sidebar<br><span class="stars">★★★★★</span></p></div>
    <div class="row"><div class="sq" role="img" aria-label="Photo thumbnail" style="background:#3a3e44"></div><p>New York Traffic Reports, Live Traffic &amp; Road Conditions</p></div>
    <div class="row"><div class="sq" role="img" aria-label="Photo thumbnail" style="background:#b98a5a"></div><p>Post slider is a convenient way to display posts from the blog</p></div>
  </div>

  <h3 class="abs side-head" style="top:1992px">Archives</h3>
  <ul class="abs side-list" style="top:2030px">
    <li>October 2014</li><li>September 2014</li><li>August 2014</li><li>July 2014</li><li>June 2014</li>
  </ul>

  <h3 class="abs side-head" style="top:2266px">Meta</h3>
  <ul class="abs side-list" style="top:2302px">
    <li>Log in</li><li>Entries RSS</li><li>Comments RSS</li><li>Pressbook.org</li>
  </ul>

  <div class="abs ad-square">advertisement<b>250 x 250</b></div>

  <div class="abs newsletter">
    <h3 style="font-size:14px;font-weight:400;color:var(--ink)">Newsletter</h3>
    <p>Trail notes, ferry times and seasonal tips for Ushuaia, once a month.</p>
    <div class="field">Your email address</div>
    <div class="btn">Sign up</div>
  </div>

  <div class="abs follow">
    <span><i class="round"></i>Zirpex +</span>
    <span><i></i>WorkTally</span>
  </div>
</aside>

<footer>
  <div class="abs footer"></div>

  <h4 class="abs f-head" style="left:128px">Most Commented</h4>
  <div class="abs" style="left:128px;top:3062px">
    <div class="f-post"><div class="sq" role="img" aria-label="Photo thumbnail" style="background:#8a6f5c"></div><p>Review post (content overflow)<br><span class="stars">★★★★★</span></p></div>
    <div class="f-post"><div class="sq" role="img" aria-label="Photo thumbnail" style="background:#5d7e9c"></div><p>Review post with sidebar<br><span class="stars">★★★★★</span></p></div>
    <div class="f-post"><div class="sq" role="img" aria-label="Photo thumbnail" style="background:#4e5a66"></div><p>New York Traffic Reports, Live Traffic &amp; Road Conditions</p></div>
    <div class="f-post"><div class="sq" role="img" aria-label="Photo thumbnail" style="background:#b98a5a"></div><p>Post slider is a convenient way to display posts from the blog front</p></div>
  </div>

  <h4 class="abs f-head" style="left:381px">Photo Stream</h4>
  <div class="abs photo-grid" role="img" aria-label="Grid of nine small travel photos">
    <div style="background:#6d5a4a"></div><div style="background:#8a7a6a"></div><div style="background:#5a6a7a"></div>
    <div style="background:#7a6a5a"></div><div style="background:#4a5a6a"></div><div style="background:#9a8a7a"></div>
    <div style="background:#5a4a3a"></div><div style="background:#6a7a8a"></div><div style="background:#8a6a5a"></div>
  </div>

  <h4 class="abs f-head" style="left:635px">Social Feed</h4>
  <div class="abs" style="left:635px;top:3062px">
    <div class="tweet"><svg width="12" height="12" viewBox="0 0 12 12"><circle cx="6" cy="6" r="6" fill="#4a8ac9"/></svg><p><span>@Ushuaia_Info</span> New trail notes for Martial Glacier posted, worth a look before you go <span>brelocanto.inf.br</span><small>1 day ago</small></p></div>
    <div class="tweet"><svg width="12" height="12" viewBox="0 0 12 12"><circle cx="6" cy="6" r="6" fill="#4a8ac9"/></svg><p><span>@Ushuaia_Info</span> Ferry times along the channel updated for the new season <span>brelocanto.inf.br</span><small>2 days ago</small></p></div>
    <div class="tweet"><svg width="12" height="12" viewBox="0 0 12 12"><circle cx="6" cy="6" r="6" fill="#4a8ac9"/></svg><p><span>@Ushuaia_Info</span> Weekend weather looks clear for the national park hikes <span>brelocanto.inf.br</span><small>3 days ago</small></p></div>
  </div>

  <h4 class="abs f-head" style="left:884px;width:190px">Weather Widget</h4>
  <div class="abs weather-now"><b>12<sup>°c</sup></b><p>Ushuaia<br>Partly cloudy<br>Wind 14 km/h<br>Humidity 72%</p></div>
  <div class="abs weather-days">
    <div>11<sup style="font-size:10px">c</sup><small>Mon</small></div>
    <div>16<sup style="font-size:10px">c</sup><small>Tue</small></div>
    <div>12<sup style="font-size:10px">c</sup><small>Wed</small></div>
  </div>

  <nav class="abs sitemap" aria-label="Sitemap">
    <div><h5>Sitemap</h5><ul><li>Home</li><li>Headers</li><li>Sliders</li></ul></div>
    <div><h5>Guide</h5><ul><li>Features</li><li>Blog</li><li>Reviews</li></ul></div>
    <div><h5>Media</h5><ul><li>Gallery</li><li>Photo Stream</li><li>Archives</li></ul></div>
    <div><h5>Follow</h5><ul><li>Zirpex +</li><li>WorkTally</li><li>Newsletter</li></ul></div>
  </nav>
  <div class="abs bottom-bar"><span>© 2014 brelocanto.inf.br</span><span>Ushuaia destination guide</span></div>
</footer>

</body>
</html>
```